Sponsorship and registration document for Charity Golf Day 2022

The project requires 2 documents to be updated to look more graphically savvy and professionally presentable.
1. Charity golf day sponsorship document
2. One page registration document.
The text has been completed. Text not to be changed - just graphics.
New images would be preferred.
The logos have been provided.

Target Market(s)

Corporate Sponsors and Golf players

Requirements
Must have
• Golf Theme

```html
<!DOCTYPE html>
<html lang="en">
<head>
<meta charset="utf-8">
<title>2022 Charity Golf Day – Registration Form</title>
<link href="https://fonts.googleapis.com/css2?family=Montserrat:wght@600;700;800&family=Arimo:wght@400;700&display=swap" rel="stylesheet">
<style>
  :root{
    --navy:#1d4a8c;
    --navy-dark:#163d78;
    --green:#5fb52a;
    --ink:#333333;
    --grey-text:#4f4f4f;
    --panel:#e2e2e2;
    --field-border:#8a8a8a;
    --paper:#ffffff;
    --orange:#f2a33a;
  }
  *{box-sizing:border-box;margin:0;padding:0}
  html,body{width:800px;height:1200px;overflow:hidden;background:var(--paper)}
  body{font-family:"Arimo",Arial,sans-serif;color:var(--ink);position:relative}

  .header{position:relative;height:150px;
    background:linear-gradient(180deg,#cfe0a4 0%,#e3edc1 55%,#f4f8ea 100%);}
  .header-photo{position:absolute;inset:0;
    background:radial-gradient(ellipse at 75% 20%,#a9cf6f 0%,rgba(169,207,111,0) 55%),
               radial-gradient(ellipse at 20% 10%,#b8d57a 0%,rgba(184,213,122,0) 60%);}
  .header-text{position:absolute;left:46px;top:26px}
  .event-title{font-family:"Montserrat",sans-serif;font-weight:800;font-size:35px;color:var(--navy);letter-spacing:.5px;line-height:1}
  .event-sub{font-weight:700;font-size:20px;color:var(--grey-text);margin-top:2px;word-spacing:2px}
  .event-venue{font-weight:700;font-size:15px;color:var(--grey-text);margin-top:12px;line-height:1.2}
  .club-name{position:absolute;right:40px;top:40px;display:flex;align-items:center;gap:10px}
  .club-name span{font-family:"Montserrat",sans-serif;font-weight:600;font-size:22px;color:var(--navy);text-align:right;line-height:1.15}
  .club-dot{width:52px;height:52px;border-radius:50%;background:var(--orange)}
  .stripe{height:8px;background:linear-gradient(90deg,var(--green) 0%,#8fcf52 60%,rgba(143,207,82,0) 78%)}

  .content{padding:22px 46px 0 46px}
  .lead{font-family:"Montserrat",sans-serif;font-weight:700;font-size:21px;color:var(--navy);line-height:1.15;width:560px}
  .tagline{font-family:"Montserrat",sans-serif;font-weight:700;font-size:13.4px;color:var(--green);margin-top:10px}
  .invite{font-family:"Montserrat",sans-serif;font-weight:700;font-size:13.4px;color:var(--navy);margin-top:10px}
  .body-copy{font-size:12.3px;line-height:1.45;margin-top:9px}

  .section-tag{display:inline-block;width:212px;background:var(--navy);color:#fff;font-family:"Montserrat",sans-serif;
    font-weight:700;font-size:13.5px;letter-spacing:.4px;padding:5px 10px;margin-top:14px}
  .price{font-family:"Montserrat",sans-serif;font-weight:700;font-size:19px;color:var(--navy);margin-top:12px}
  .price-note{font-size:13px;margin-top:6px}

  .schedule{display:grid;grid-template-columns:1fr 1fr;background:var(--panel);margin-top:10px;padding:8px 4px 8px 3px;
    font-family:"Montserrat",sans-serif;font-weight:600;font-size:12.4px;color:var(--grey-text);row-gap:7px}
  .schedule ul{list-style:none;display:grid;row-gap:8px}
  .schedule b{color:var(--navy);font-weight:700;display:inline-block;width:70px}
  .schedule .right{padding-left:84px}

  .instruction{font-size:15px;margin-top:20px}
  .instruction strong{font-weight:700}

  .details{margin-top:18px;display:grid;grid-template-columns:172px 1fr;row-gap:14px;align-items:center;
    font-weight:700;font-size:15.5px;color:var(--grey-text)}
  .field{height:19px;border:1.5px solid var(--field-border);background:#fff}
  .contact-row{display:flex;align-items:center;gap:22px}
  .contact-row .field.short{width:168px}
  .contact-row .field.wide{flex:1}

  .team{margin-top:22px;display:grid;grid-template-columns:186px 186px 134px 50px 1fr;column-gap:9px;row-gap:4px}
  .team-head{background:var(--navy);color:#fff;font-family:"Montserrat",sans-serif;font-weight:700;font-size:14px;
    letter-spacing:.5px;padding:3px 4px;height:23px;display:flex;align-items:center}
  .team-head.small{font-size:7.5px;justify-content:center;padding:3px 1px}
  .team .field{height:18px}
  .team-head + .team-head{}
  .note{font-size:10.2px;margin-top:10px}

  .totals{display:flex;align-items:center;margin-top:10px;font-family:"Montserrat",sans-serif;font-weight:700;font-size:13px;color:var(--navy)}
  .totals .box{border:1.5px solid var(--field-border);font-family:"Arimo",sans-serif;font-weight:400;font-size:10px;color:var(--ink);padding:2px 4px;height:19px;margin-left:8px}
  .totals .cost-box{width:96px}
  .totals .total-box{width:96px}
  .totals .total-label{margin-left:68px}

  .pay-tag{width:344px;font-weight:700}
  .pay-tag span{font-weight:600}
  .payment{display:grid;grid-template-columns:420px 1fr;margin-top:12px;font-size:12.6px;line-height:1.35}
  .option{display:flex;gap:12px}
  .tick{width:22px;height:22px;background:#cfcfcf;flex:none;margin-top:2px}
  .eft{display:grid;grid-template-columns:104px auto}

  .terms{background:var(--panel);margin-top:16px;padding:4px 7px;font-size:9.2px;line-height:1.3}
</style>
</head>
<body>
  <header class="header">
    <div class="header-photo" role="img" aria-label="Soft-focus photo of a sunlit golf course fairway"></div>
    <div class="header-text">
      <h1 class="event-title">2022 CHARITY GOLF DAY</h1>
      <p class="event-sub">FRIDAY 25 MARCH 2022 &nbsp; I ELMWOOD GOLF CLUB</p>
      <p class="event-venue">48 Linden Road, East Elmwood<br>www.pvsc.org.au/golf-day</p>
    </div>
    <div class="club-name">
      <span>Parkview<br>Service Club</span>
      <div class="club-dot"></div>
    </div>
  </header>
  <div class="stripe"></div>

  <main class="content">
    <h2 class="lead">Do you care about prostate cancer and fighting this disease?</h2>
    <p class="tagline">Help us hit prostate cancer off the green and beat the most common cancer in Australian men.</p>
    <p class="invite">Enter a team or as an individual in the 2022 Charity Golf Day.</p>
    <p class="body-copy">Proceeds from this event will be donated to Prostate Cancer Research Group at the Southbank Discovery Institute, Eastgate University, to fund world leading, innovative research and to support men and their families affected by prostate cancer.</p>

    <div class="section-tag">COST INFORMATION</div>
    <p class="price">$ 150 per player</p>
    <p class="price-note">Cost includes golf, light breakfast with coffee / tea on arrival and a two – course lunch following the game.</p>

    <div class="section-tag">EVENT INFORMATION</div>
    <div class="schedule">
      <ul>
        <li><b style="width:auto">Event:&nbsp; 4 person Ambrose</b></li>
        <li><b>7:00am:</b>Registration</li>
        <li><b>7:15am:</b>Breakfast</li>
        <li><b>7:45am:</b>Briefing</li>
      </ul>
      <ul class="right">
        <li><b>8:00am:</b>Shotgun start</li>
        <li><b>12.30pm:</b>Lunch</li>
        <li><b>2.00pm:</b>Presentation/Prizes</li>
        <li><b>3.00pm:</b>Finish</li>
      </ul>
    </div>

    <div class="section-tag">REGISTRATION FORM</div>
    <p class="instruction">Please complete the details below and return via e-mail to <strong>events@pvsc-mail.org</strong></p>

    <div class="details">
      <span>NAME:</span><div class="field"></div>
      <span>ORGANISATION:</span><div class="field"></div>
      <span>ADDRESS:</span><div class="field"></div>
      <span>MOBILE:</span>
      <div class="contact-row"><div class="field short"></div><span>EMAIL:</span><div class="field wide"></div></div>
    </div>

    <div class="team">
      <div class="team-head">NAME</div>
      <div class="team-head">EMAIL</div>
      <div class="team-head">MOBIE</div>
      <div class="team-head small">GAH'CAP</div>
      <div class="team-head">GOLF ID NO.</div>
      <div class="field"></div><div class="field"></div><div class="field"></div><div class="field"></div><div class="field"></div>
      <div class="field"></div><div class="field"></div><div class="field"></div><div class="field"></div><div class="field"></div>
      <div class="field"></div><div class="field"></div><div class="field"></div><div class="field"></div><div class="field"></div>
      <div class="field"></div><div class="field"></div><div class="field"></div><div class="field"></div><div class="field"></div>
    </div>
    <p class="note">*Please Note: Players without an official club Handicap will be given a maximum handicap of 27 (Men) and 36 (Ladies)</p>

    <div class="totals">
      <span>COST:</span><div class="box cost-box">$150 per player</div>
      <span class="total-label">TOTAL:</span><div class="box total-box">$</div>
    </div>

    <div class="section-tag pay-tag">METHOD OF PAYMMENT <span>(please tick)</span></div>
    <div class="payment">
      <div class="option">
        <div class="tick"></div>
        <p>Cheque payable to Parkview Service Club<br>Form and cheque can be mailed to Marla Venturi,<br>c/- &nbsp;PO Box 412, Hillcrest Vic 3199</p>
      </div>
      <div class="option">
        <div class="tick"></div>
        <div class="eft">
          <span>EFT</span><span></span>
          <span>BSB:</span><span>600 100</span>
          <span>Account No:</span><span>123 456 789</span>
          <span>Comment:</span><span>PVSCGolf and your surname</span>
        </div>
      </div>
    </div>

    <p class="terms">CANCELLATIONS: Fees are non-refundable or transferable. Substitutions can be made in writing addressed to Marla via email to events@pvsc-mail.org. PVSC will only reimburse registration fees if the event is cancelled. PVSC is not responsible for any costs incurred as a result. Non-Attendance: If a player fails to attend, fees will not be refunded or allocated to another event.</p>
  </main>
</body>
</html>
```